Cardinal Lino Baraza Conferencia

We need a postcard 5 x 7 inches to promote a visit in our Catholic parish, from Cardinal Lino Baraza of El Salvador. We want a Catholic content/background, and a nice picture of the Cardinal, which you can find in findora. Cardinal will be giving Mass and will be giving a conference talk after the Mass. He will give Mass at 7pm at Saint Vesper Hollow Catholic Church, 51972 Oren Malk Pkwy, Sterling, VA 20187, and then he will be giving a talk afterwards at Marrowind Hall, which is a hall in the parish. Please put the following in Spanish. "Misa 7pm," "Conferencia 7:45pm (en Marrowind Hall)" The conference title should be "Familia, Iglesia doméstica y transmisora de la fe" And also add that there will be refreshments after the talk at "Café y Pan Dulce 9pm" The date is "Jueves, Agosto 17, 2023"

```html
<!DOCTYPE html>
<html lang="es">
<head>
<meta charset="utf-8">
<title>Familia, Iglesia Doméstica y Transmisora de la Fe — Postal</title>
<link href="https://fonts.googleapis.com/css2?family=Oswald:wght@600;700&family=Hind:wght@400;500;600;700&display=swap" rel="stylesheet">
<style>
  :root {
    --navy: #1f3d73;
    --navy-deep: #173262;
    --ink: #3a3a3a;
    --yellow: #ffd21f;
    --paper: #ffffff;
    --paper-shade: #e9eaec;
    --backdrop: #7b7b7b;
  }
  * { margin: 0; padding: 0; box-sizing: border-box; }
  html, body { width: 1200px; height: 904px; overflow: hidden; background: var(--backdrop); }
  .postcard {
    position: absolute; left: 0; top: 24px;
    width: 1200px; height: 857px;
    overflow: hidden;
    background: linear-gradient(180deg, var(--paper) 0%, var(--paper) 40%, var(--paper-shade) 100%);
    font-family: "Hind", Arial, sans-serif;
  }
  .postcard__shapes { position: absolute; inset: 0; }
  .headline {
    position: absolute; left: 50px; top: 38px;
    font-family: "Oswald", "Arial Narrow", sans-serif;
    font-weight: 700; font-size: 60px; line-height: 71px;
    text-transform: uppercase; letter-spacing: -0.5px;
  }
  .headline span { display: block; }
  .headline .navy { color: var(--navy); }
  .headline .ink { color: var(--ink); }
  .schedule {
    position: absolute; left: 50px; top: 378px;
    color: var(--paper); font-weight: 600;
  }
  .schedule__line { font-size: 35px; line-height: 44px; }
  .schedule__line em { font-style: normal; color: var(--yellow); }
  .schedule__note { font-size: 27px; font-weight: 500; line-height: 34px; }
  .date-row { position: absolute; left: 48px; top: 548px; display: flex; align-items: center; }
  .date-row__day {
    font-family: "Oswald", "Arial Narrow", sans-serif; font-weight: 600;
    font-size: 76px; line-height: 80px; color: var(--navy);
    margin-left: 16px; padding-right: 10px;
    border-right: 3px solid var(--yellow);
  }
  .date-row__text {
    margin-left: 12px; font-weight: 700; font-size: 26px; line-height: 32px;
    text-transform: uppercase;
  }
  .date-row__text .navy { color: var(--navy); }
  .date-row__text .ink { color: var(--ink); }
  .venue-row { position: absolute; left: 48px; top: 654px; display: flex; align-items: center; }
  .venue-row__text { margin-left: 16px; }
  .venue-row__name { font-size: 28px; font-weight: 700; color: var(--navy); line-height: 32px; }
  .venue-row__address { font-size: 21px; font-weight: 600; color: #222; line-height: 26px; }
  .treat-row { position: absolute; left: 48px; top: 763px; display: flex; align-items: center; }
  .treat-row__text { margin-left: 16px; font-size: 37px; font-weight: 500; color: var(--paper); }
  .badge { width: 76px; height: 76px; flex: none; }
</style>
</head>
<body>
<main class="postcard">
  <svg class="postcard__shapes" width="1200" height="857" viewBox="0 0 1200 857">
    <defs>
      <linearGradient id="ghostTone" x1="0" y1="0" x2="1" y2="1">
        <stop offset="0" stop-color="#f3f3f3"/>
        <stop offset="0.5" stop-color="#d6d6d6"/>
        <stop offset="1" stop-color="#ececec"/>
      </linearGradient>
      <linearGradient id="portraitTone" x1="0" y1="0" x2="1" y2="1">
        <stop offset="0" stop-color="#3b2a26"/>
        <stop offset="0.45" stop-color="#7a3a2a"/>
        <stop offset="0.7" stop-color="#e2502a"/>
        <stop offset="1" stop-color="#f4ece6"/>
      </linearGradient>
    </defs>
    <!-- faded speaker portrait behind text -->
    <polygon points="420,150 700,150 754,426 640,645 420,645" fill="url(#ghostTone)" role="img" aria-label="Faded grayscale photo of Cardinal Lino Baraza speaking into a microphone"/>
    <!-- white location band -->
    <rect x="0" y="645" width="620" height="102" fill="var(--paper)"/>
    <!-- navy chevron stripe -->
    <polygon points="542,0 700,0 800,426 700,857 535,857 754,426" fill="var(--navy)"/>
    <!-- main portrait -->
    <polygon points="613,0 1200,0 1200,857 660,857 770,426" fill="url(#portraitTone)" role="img" aria-label="Photo of Cardinal Lino Baraza in red vestments and biretta"/>
    <!-- schedule banner -->
    <polygon points="0,362 945,362 0,362" fill="none"/>
    <polygon points="0,362 386,362 419,446 386,529 0,529" fill="var(--navy)"/>
    <!-- refreshments band -->
    <polygon points="0,747 584,747 535,857 0,857" fill="var(--navy)"/>
  </svg>

  <h1 class="headline">
    <span class="navy">Familia, Iglesia</span>
    <span class="ink">Doméstica y</span>
    <span class="navy">Transmisora</span>
    <span class="ink">de la fe</span>
  </h1>

  <section class="schedule">
    <p class="schedule__line">MISA <em>7PM</em></p>
    <p class="schedule__line">Conference <em>7 : 45pm</em></p>
    <p class="schedule__note">(in Marrowind Hall)</p>
  </section>

  <section class="date-row">
    <svg class="badge" viewBox="0 0 76 76" aria-hidden="true">
      <circle cx="38" cy="38" r="36" fill="var(--navy)"/>
      <circle cx="38" cy="38" r="31" fill="none" stroke="#fff" stroke-width="2"/>
      <rect x="22" y="25" width="32" height="28" rx="3" fill="none" stroke="#fff" stroke-width="3"/>
      <line x1="22" y1="33" x2="54" y2="33" stroke="#fff" stroke-width="3"/>
      <line x1="29" y1="20" x2="29" y2="28" stroke="#fff" stroke-width="3"/>
      <line x1="47" y1="20" x2="47" y2="28" stroke="#fff" stroke-width="3"/>
      <g fill="#fff">
        <rect x="27" y="38" width="5" height="4"/><rect x="35.5" y="38" width="5" height="4"/><rect x="44" y="38" width="5" height="4"/>
        <rect x="27" y="45" width="5" height="4"/><rect x="35.5" y="45" width="5" height="4"/><rect x="44" y="45" width="5" height="4"/>
      </g>
    </svg>
    <span class="date-row__day">17</span>
    <p class="date-row__text"><span class="navy">Jueves,</span><br><span class="ink">Agosto, 2023</span></p>
  </section>

  <section class="venue-row">
    <svg class="badge" viewBox="0 0 76 76" aria-hidden="true">
      <circle cx="38" cy="38" r="36" fill="var(--navy)"/>
      <circle cx="38" cy="38" r="31" fill="none" stroke="#fff" stroke-width="2"/>
      <path d="M38 54 C30 44 27 39 27 33 a11 11 0 0 1 22 0 c0 6 -3 11 -11 21z" fill="none" stroke="#fff" stroke-width="3"/>
      <circle cx="38" cy="33" r="4" fill="none" stroke="#fff" stroke-width="3"/>
      <ellipse cx="38" cy="55" rx="13" ry="4" fill="none" stroke="#fff" stroke-width="2.5"/>
    </svg>
    <div class="venue-row__text">
      <p class="venue-row__name">Iglesia Católica Saint Vesper Hollow</p>
      <p class="venue-row__address">51972 Oren Malk Pkwy, Sterling, VA 20187</p>
    </div>
  </section>

  <section class="treat-row">
    <svg class="badge" viewBox="0 0 76 76" aria-hidden="true">
      <circle cx="38" cy="38" r="36" fill="var(--yellow)"/>
      <circle cx="38" cy="38" r="30" fill="#fff"/>
      <path d="M24 36 h24 v8 a10 10 0 0 1 -10 10 h-4 a10 10 0 0 1 -10 -10z" fill="none" stroke="var(--navy)" stroke-width="2.5"/>
      <path d="M48 39 h3 a4 4 0 0 1 0 8 h-4" fill="none" stroke="var(--navy)" stroke-width="2.5"/>
      <line x1="20" y1="57" x2="56" y2="57" stroke="var(--navy)" stroke-width="2.5"/>
      <path d="M31 30 q-2 -3 0 -6 M37 30 q-2 -3 0 -6 M43 30 q-2 -3 0 -6" fill="none" stroke="var(--navy)" stroke-width="2"/>
    </svg>
    <p class="treat-row__text">Café y Pan Dulce 9pm</p>
  </section>
</main>
</body>
</html>
```